Business card for apparel company. Specializing in fishing and boating performance wear. Main company name is Marlowe Teal Company, LLC brand name for apparel is WAKEFIN. See website www.WakefinReefline.com I will attach some logos to consider.

```html
<!DOCTYPE html>
<html lang="en">
<head>
<meta charset="utf-8">
<title>Wakefin Business Card</title>
<link rel="stylesheet" href="https://fonts.googleapis.com/css2?family=Poppins:wght@400;500;700;800&display=swap">
<style>
  :root {
    --page: #e6e8eb;
    --slate: #3f4d5e;
    --slate-deep: #36414f;
    --brand-blue: #2f6fc0;
    --sky: #1ba7e0;
    --ink-blue: #2d63b4;
    --white: #ffffff;
    --wave-grey: #4a5868;
  }
  * { box-sizing: border-box; margin: 0; padding: 0; }
  html, body {
    width: 1200px; height: 900px; overflow: hidden;
    background: var(--page);
    font-family: "Poppins", sans-serif;
  }
  .card {
    position: absolute;
    left: 290px;
    width: 620px; height: 354px;
    border-radius: 22px;
    overflow: hidden;
    box-shadow: 0 10px 28px rgba(0,0,0,.18);
  }
  /* Back side */
  .card-back {
    top: 70px;
    background: linear-gradient(135deg, var(--slate) 0%, var(--slate-deep) 100%);
    color: var(--white);
  }
  .back-brand {
    position: absolute; left: 0; right: 0; top: 120px;
    display: flex; align-items: center; justify-content: center; gap: 16px;
  }
  .brand-dot {
    width: 30px; height: 30px; border-radius: 50%;
    border: 3px solid currentColor;
  }
  .back-brand .brand-name {
    font-weight: 800; font-size: 46px; letter-spacing: 4px;
  }
  .back-url {
    position: absolute; left: 0; right: 0; bottom: 46px;
    text-align: center;
    font-weight: 700; font-size: 17px; letter-spacing: 3px; text-transform: uppercase;
  }
  /* Front side */
  .card-front {
    top: 476px;
    background: var(--white);
  }
  .front-wave { position: absolute; inset: 0; width: 100%; height: 100%; }
  .front-brand {
    position: absolute; left: 44px; top: 96px;
    display: flex; align-items: center; gap: 14px;
    color: var(--brand-blue);
  }
  .front-brand .brand-name {
    font-weight: 800; font-size: 52px; letter-spacing: 3px; line-height: 1;
  }
  .contact {
    position: absolute; right: 30px; top: 26px;
    text-align: right; color: var(--ink-blue);
  }
  .contact-name {
    font-weight: 700; font-size: 21px; letter-spacing: 1px; margin-right: 24px;
  }
  .contact-line {
    display: flex; align-items: center; justify-content: flex-end; gap: 8px;
    font-size: 13px; line-height: 20px;
  }
  .contact-line svg { width: 14px; height: 14px; flex: none; }
  .address {
    position: absolute; right: 34px; bottom: 58px;
    text-align: right; color: var(--white);
    font-weight: 500; font-size: 15px; line-height: 22px;
  }
</style>
</head>
<body>

<section class="card card-back">
  <div class="back-brand">
    <span class="brand-dot"></span>
    <span class="brand-name">WAKEFIN</span>
  </div>
  <p class="back-url">www.WakefinReefline.com</p>
</section>

<section class="card card-front">
  <svg class="front-wave" viewBox="0 0 620 354" preserveAspectRatio="none" aria-hidden="true">
    <defs>
      <linearGradient id="sea" x1="0" y1="1" x2="1" y2="0">
        <stop offset="0" stop-color="#2f6fc0"/>
        <stop offset=".5" stop-color="#1ba7e0"/>
        <stop offset="1" stop-color="#2f6fc0"/>
      </linearGradient>
    </defs>
    <path d="M0,252 C160,262 300,244 390,200 C470,160 545,136 620,132 L620,144 C548,150 482,172 412,214 C322,270 170,284 0,282 Z" fill="var(--wave-grey)"/>
    <path d="M0,294 C170,300 322,276 422,222 C502,178 562,160 620,156 L620,354 L0,354 Z" fill="url(#sea)"/>
    <path d="M150,346 C260,338 330,318 392,282 C340,322 260,342 150,346 Z" fill="var(--white)"/>
  </svg>

  <div class="front-brand">
    <span class="brand-dot"></span>
    <span class="brand-name">WAKEFIN</span>
  </div>

  <div class="contact">
    <p class="contact-name">JORDAN REYES</p>
    <p class="contact-line">0135-246-578
      <svg viewBox="0 0 24 24"><path d="M6.6 10.8a15 15 0 0 0 6.6 6.6l2.2-2.2a1 1 0 0 1 1-.25 11.4 11.4 0 0 0 3.6.57 1 1 0 0 1 1 1V20a1 1 0 0 1-1 1A17 17 0 0 1 3 4a1 1 0 0 1 1-1h3.5a1 1 0 0 1 1 1c0 1.25.2 2.45.57 3.570a1 1 0 0 1-.25 1z" fill="var(--wave-grey)"/></svg>
    </p>
    <p class="contact-line">info@MarloweTealCo.com
      <svg viewBox="0 0 24 24"><rect x="2" y="5" width="20" height="14" rx="1" fill="var(--wave-grey)"/><path d="M2 6l10 7 10-7" stroke="#fff" stroke-width="1.6" fill="none"/></svg>
    </p>
    <p class="contact-line">www.WakefinReefline.com
      <svg viewBox="0 0 24 24"><g fill="none" stroke="var(--wave-grey)" stroke-width="2"><circle cx="12" cy="12" r="9"/><path d="M3 12h18M12 3c3 3 3 15 0 18M12 3c-3 3-3 15 0 18"/></g></svg>
    </p>
  </div>

  <p class="address">P.O. Box 418, Carver Bay<br>Florida 34712</p>
</section>

</body>
</html>
```